Business letterhead and powerpoint template

Hi, I have recently started using a new logo (found through PixelGrove) and would now like to use that logo for letterheads and powerpoint.

Attached is the logo and one version of a brochure I have recently used.

Industry/Entity Type

Business

```html
<!DOCTYPE html>
<html lang="en">
<head>
<meta charset="utf-8">
<title>Halvern Capital Letterhead</title>
<link rel="stylesheet" href="https://fonts.googleapis.com/css2?family=Source+Sans+3:wght@400;600&display=swap">
<style>
  :root {
    --page: #f7f7f7;
    --ink: #2b2b2b;
    --rule: #b9b9b9;
    --brand-ink: #3d3d3d;
    --accent: #d2553a;
    --signature-area: #ececec;
  }
  * { margin: 0; padding: 0; box-sizing: border-box; }
  html, body { width: 847px; height: 1200px; overflow: hidden; }
  body {
    background: var(--page);
    font-family: "Source Sans 3", sans-serif;
    color: var(--ink);
    position: relative;
  }
  .letterhead { position: absolute; inset: 0; }
  .brand {
    position: absolute; left: 66px; top: 88px;
    display: flex; align-items: center; gap: 12px;
  }
  .brand-dot { width: 22px; height: 22px; border-radius: 50%; background: var(--accent); }
  .brand-name {
    font-size: 40px; font-weight: 400; letter-spacing: 1px;
    color: var(--brand-ink); line-height: 1;
  }
  .header-rule {
    position: absolute; left: 66px; right: 33px; top: 138px;
    height: 2px; background: var(--rule);
  }
  .letter {
    position: absolute; left: 87px; top: 246px; width: 720px;
    font-size: 16px; line-height: 20px;
  }
  .letter p { margin-bottom: 20px; }
  .letter .body-main { margin-bottom: 62px; }
  .signature {
    position: absolute; left: 548px; top: 842px; width: 236px; height: 178px;
    background: var(--signature-area);
  }
  .footer {
    position: absolute; left: 47px; right: 53px; top: 1136px;
    text-align: center; font-size: 11px; font-weight: 600; color: var(--ink);
  }
  .footer svg { vertical-align: -2px; }
  .footer-rule {
    position: absolute; left: 47px; right: 53px; top: 1162px;
    height: 1px; background: var(--rule);
  }
</style>
</head>
<body>
<main class="letterhead">
  <header>
    <div class="brand">
      <span class="brand-dot"></span>
      <span class="brand-name">HALVERN CAPITAL</span>
    </div>
    <div class="header-rule"></div>
  </header>

  <section class="letter">
    <p>2750, Cedar Hollow Road<br>Pasadena, CA 91101.</p>
    <p>January 29th, 2011</p>
    <p>Mr. Whitaker<br>President, Whitaker Youth Center<br>518 Linden Avenue<br>Albany, NY 12203</p>
    <p>Dear Mr. Whitaker:</p>
    <p class="body-main">In the first paragraph, one needs to give a brief introduction of oneself. One should also give reference to the purpose of the letter in brief.<br>
    The second paragraph needs to give the details of the letter and its need. This paragraph is mostly longer than the others and plays the main role in the letter. Keep the sentences short and to the point. Avoid using complex words and sentences.</p>
    <p>The third and last paragraph is the conclusion of the letter and can be kept short.</p>
    <p>Sincerely,</p>
    <p>(this is where the signature of the writer will be placed)</p>
    <p>Morgan Ellery<br>Read more at Letterwise: http://www.letterwise.net/articles/professional-letter-format-example.html</p>
  </section>

  <div class="signature" role="img" aria-label="Handwritten signature of the letter writer"></div>

  <footer>
    <p class="footer">Meridian Plaza, 240 Harbour Street, 18th Floor PO Box 312 Toronto, Ontario M5J 1A7 |
      <svg width="11" height="11" viewBox="0 0 24 24" aria-hidden="true"><path fill="currentColor" d="M6.6 10.8a15 15 0 0 0 6.6 6.6l2.2-2.2a1 1 0 0 1 1-.25 11.4 11.4 0 0 0 3.6.57 1 1 0 0 1 1 1V20a1 1 0 0 1-1 1A17 17 0 0 1 3 4a1 1 0 0 1 1-1h3.5a1 1 0 0 1 1 1c0 1.25.2 2.45.57 3.57a1 1 0 0 1-.25 1z"/></svg>1-800-555-0142 | www.halvernlegal.ca</p>
    <div class="footer-rule"></div>
  </footer>
</main>
</body>
</html>
```